Consulting company needs website design

We need a simple, static website design for our consulting company. We are looking for a general design of the look and feel of the website. Initially, it will have these pages:
- Home
- About us
- Services
- Contact us
We have our own logo which I have attached to the brief.

We are looking for a simple website, with white background and the use of gray (darker) as the main theme. Simple fonts. The website should be responsive so it an be easily red in mobile devices.

As part of the project, we will need to receive at least the following items:
- Individual files with sample text to support the pages outlined above
- Necessary CSS files

Our current website is here: http://www.marlowvane.co/

Here are some examples of other website we like to be used as guideline:
- http://www.tornaviamundo.com/
-

Target Market(s)

Individuals and companies looking to hire our company to provide consulting services.

Industry/Entity Type

It Company

Coding

Coded - Design and coding required

Number of Pages Required

4 page

Font styles to use
Sans Serif

Requirements
Must have
• Main page should have the ability to embed Chirply feed into it.
• We prefer the design to use gray tones.

```html
<!DOCTYPE html>
<html lang="en">
<head>
<meta charset="utf-8">
<title>Marlow Vane Group — Consulting</title>
<link rel="stylesheet" href="https://fonts.googleapis.com/css2?family=Raleway:wght@400;500;600;700;800&family=Roboto:ital,wght@0,300;0,400;0,500;1,300;1,400&display=swap">
<style>
:root{
  --ink:#222326;
  --text:#4a4a4a;
  --muted:#8a8a8a;
  --line:#e3e3e3;
  --dark:#3a3a3c;
  --darker:#2a2a2b;
  --footer-bar:#1e1e1f;
  --band:#efefef;
  --accent:#2eb3e8;
  --accent-text:#1f9fd6;
  --white:#ffffff;
}
*{box-sizing:border-box;margin:0;padding:0}
html,body{width:1200px;height:2466px;overflow:hidden;background:var(--white)}
body{position:relative;font-family:"Roboto",sans-serif;color:var(--text)}
.abs{position:absolute}
.raleway{font-family:"Raleway",sans-serif}

/* header */
.site-header{position:absolute;left:0;top:0;width:1200px;height:133px;background:var(--white)}
.brand{position:absolute;left:95px;top:26px;width:170px;text-align:center}
.brand-mark{display:block;margin:0 auto 8px;width:56px;height:56px;border:2px solid #9a9a9a;border-radius:50%}
.brand-name{font-family:"Raleway",sans-serif;font-weight:700;font-size:19px;color:var(--ink)}
.util-nav{position:absolute;top:34px;left:633px;display:flex;gap:28px;font-size:12px;color:#555}
.btn-quote{position:absolute;left:988px;top:26px;width:112px;height:36px;background:#333335;color:#fff;border-radius:3px;font-size:13px;font-weight:500;display:flex;align-items:center;justify-content:center}
.main-nav{position:absolute;top:88px;left:406px;display:flex;gap:0;font-family:"Raleway",sans-serif;font-size:14px;color:#555}
.main-nav span{margin-right:50px}
.main-nav span:last-child{margin-right:0}
.main-nav .active{color:var(--ink);font-weight:600}

/* hero */
.hero{position:absolute;left:0;top:133px;width:1200px;height:536px;background:linear-gradient(100deg,#8d8e92 0%,#b9b7b4 30%,#6b6d73 60%,#3d3f45 100%)}
.hero-title{position:absolute;top:222px;width:100%;text-align:center;font-family:"Raleway",sans-serif;font-weight:800;font-size:44px;color:#fff;text-shadow:0 2px 4px rgba(0,0,0,.5)}
.hero-sub{position:absolute;top:288px;width:100%;text-align:center;font-family:"Roboto",sans-serif;font-weight:500;font-size:32px;color:#fff;text-shadow:0 2px 4px rgba(0,0,0,.5)}
.hero-arrow{position:absolute;top:238px;width:40px;height:40px}
.shadow-curve{position:absolute;left:150px;width:900px;height:30px;background:radial-gradient(ellipse at 50% 0,rgba(0,0,0,.18),rgba(0,0,0,0) 70%)}

/* intro */
.section-title{position:absolute;width:1200px;text-align:center;font-family:"Raleway",sans-serif;font-size:26px;color:var(--ink)}
.section-sub{position:absolute;width:1200px;text-align:center;font-size:13px;color:#555}
.insight{position:absolute;top:804px;width:296px}
.insight-kicker{font-size:12px;color:#666}
.insight-title{margin-top:10px;font-family:"Raleway",sans-serif;font-size:21px;color:var(--ink)}
.insight-title b{font-weight:800}
.insight-text{margin-top:18px;font-size:11.5px;font-style:italic;font-weight:300;line-height:21px;color:var(--muted)}
.col-rule{position:absolute;top:806px;width:1px;height:130px;background:var(--line)}

/* stats */
.stats-photo{position:absolute;left:0;top:983px;width:600px;height:383px;background:linear-gradient(135deg,#5f6166 0%,#2f3034 55%,#1d1e21 100%)}
.stats-panel{position:absolute;left:600px;top:983px;width:600px;height:383px;background:var(--dark);color:#fff}
.stats-kicker{position:absolute;left:71px;top:71px;font-size:13px}
.stats-title{position:absolute;left:71px;top:96px;font-family:"Raleway",sans-serif;font-size:25px}
.stats-text{position:absolute;left:71px;top:146px;width:440px;font-size:11.5px;font-style:italic;line-height:22px;color:#e6e6e6}
.stat{position:absolute;top:245px;width:160px;text-align:center}
.stat-num{font-size:36px;font-weight:500}
.stat-label{margin-top:6px;font-size:13.5px}

/* who we are */
.feed{position:absolute;left:99px;top:1516px;width:473px}
.feed-head{position:relative;height:34px;border-bottom:2px solid var(--accent)}
.feed-title{position:absolute;left:4px;top:6px;font-family:"Raleway",sans-serif;font-size:20px;color:var(--ink)}
.btn-follow{position:absolute;right:0;top:0;width:143px;height:34px;background:var(--accent);color:#fff;font-size:14px;display:flex;align-items:center;justify-content:center}
.feed-item{position:absolute;left:0;width:473px}
.feed-icon{position:absolute;left:2px;top:0;width:42px;height:42px}
.feed-name{position:absolute;left:72px;top:0;font-family:"Raleway",sans-serif;font-size:18px;color:var(--accent-text)}
.feed-text{position:absolute;left:72px;top:32px;width:400px;font-size:11.5px;font-style:italic;line-height:20px;color:#2d6b86}
.quote-card{position:absolute;left:626px;top:1506px;width:474px;height:265px;background:#f3f3f3;border:1px solid #e6e6e6}
.quote-photo{position:absolute;left:653px;top:1532px;width:197px;height:262px;background:linear-gradient(180deg,#d9d9d9,#9e9e9e);border:4px solid #8c8c8c}
.quote-open,.quote-close{position:absolute;width:24px;height:20px}
.quote-text{position:absolute;left:881px;top:1568px;width:194px;font-size:13.5px;font-style:italic;font-weight:300;line-height:23px;color:#777;text-align:justify}

/* partners */
.partners{position:absolute;left:0;top:1863px;width:1200px;height:253px;background:var(--band)}
.partners-title{position:absolute;top:46px;width:100%;text-align:center;font-family:"Raleway",sans-serif;font-size:26px;color:var(--ink)}
.partner-badge{position:absolute;top:130px;height:66px;background:#c4c4c4;border-radius:6px}

/* footer */
.site-footer{position:absolute;left:0;top:2116px;width:1200px;height:288px;background:var(--darker);overflow:hidden;color:#fff}
.footer-curve{position:absolute;left:420px;top:-180px;width:1100px;height:1100px;border-radius:50%;background:#1c1c1d}
.footer-heading{position:absolute;font-family:"Raleway",sans-serif;font-size:21px}
.footer-label{position:absolute;font-size:16px}
.footer-text{position:absolute;font-size:11.5px;line-height:20px;color:#a5a5a5}
.phone-badge{position:absolute;left:507px;top:102px;width:72px;height:72px}
.mail-input{position:absolute;left:723px;top:141px;width:349px;height:41px;border:1px solid #8a8a8a;border-radius:3px;font-size:11.5px;color:#9a9a9a;padding:12px 14px}
.btn-subscribe{position:absolute;left:723px;top:195px;width:349px;height:43px;border:1px solid #cfcfcf;border-radius:3px;font-size:17px;display:flex;align-items:center;justify-content:center}
.footer-bar{position:absolute;left:0;top:2404px;width:1200px;height:62px;background:var(--footer-bar);color:#ddd;font-size:12px;display:flex;align-items:center;justify-content:center}
</style>
</head>
<body>

<header class="site-header">
  <div class="brand">
    <span class="brand-mark"></span>
    <span class="brand-name">Marlow Vane Group</span>
  </div>
  <nav class="util-nav"><span>FAQ's</span><span>Testimonial</span><span>Help</span><span>Login</span><span>Register</span></nav>
  <div class="btn-quote">Get A Quote</div>
  <nav class="main-nav">
    <span class="active">HOME</span><span>ABOUT US</span><span>WHO WE ARE</span><span>WHAT WE DO</span><span>OUR SERVICE</span><span>CONTACT US</span>
  </nav>
</header>

<section class="hero" role="img" aria-label="Photo of business consultants smiling in a meeting around a table">
  <svg class="hero-arrow" style="left:21px" viewBox="0 0 40 40"><circle cx="20" cy="20" r="18" fill="none" stroke="#fff" stroke-width="2" opacity=".8"/><path d="M23 12 L15 20 L23 28" fill="none" stroke="#fff" stroke-width="2"/></svg>
  <svg class="hero-arrow" style="left:1136px" viewBox="0 0 40 40"><circle cx="20" cy="20" r="18" fill="none" stroke="#fff" stroke-width="2" opacity=".8"/><path d="M17 12 L25 20 L17 28" fill="none" stroke="#fff" stroke-width="2"/></svg>
  <h1 class="hero-title">WELCOME TO MARLOW VANE GROUP</h1>
  <p class="hero-sub">Future proofing your Analytics &amp; Data Science skills</p>
</section>
<div class="shadow-curve" style="top:669px"></div>

<section class="intro">
  <h2 class="section-title" style="top:714px"><b style="font-weight:800">Hello,</b> We Are Marlow Vane Group</h2>
  <p class="section-sub" style="top:754px">Great Insights About Data &amp; Analytics</p>
  <article class="insight" style="left:99px">
    <div class="insight-kicker">Unique Insight</div>
    <h3 class="insight-title"><b>01 .</b> Research</h3>
    <p class="insight-text">It is a long established fact that a reader will be distract by the readable content of a page when looking at its layout.It is a long established fact that a reader</p>
  </article>
  <div class="col-rule" style="left:418px"></div>
  <article class="insight" style="left:452px">
    <div class="insight-kicker">Unique Insight</div>
    <h3 class="insight-title"><b>02 .</b> Personalised</h3>
    <p class="insight-text">It is a long established fact that a reader will be distract by the readable content of a page when looking at its layout.It is a long established fact that a reader</p>
  </article>
  <div class="col-rule" style="left:775px"></div>
  <article class="insight" style="left:807px">
    <div class="insight-kicker">Unique Insight</div>
    <h3 class="insight-title"><b>03 .</b> Tangible Difference</h3>
    <p class="insight-text">It is a long established fact that a reader will be distract by the readable content of a page when looking at its layout.It is a long established fact that a reader</p>
  </article>
</section>

<div class="stats-photo" role="img" aria-label="Photo of hands on a tablet with floating analytics charts"></div>
<section class="stats-panel">
  <div class="stats-kicker">We Are Awesomeness</div>
  <h2 class="stats-title">Meet Our Company Statics</h2>
  <p class="stats-text">There are many variations of passages of Lorem Ipsum available, but the majority have suffered alteration in some form, by injected humour, or randomised</p>
  <div class="stat" style="left:50px"><div class="stat-num">3314</div><div class="stat-label">Information Quality</div></div>
  <div class="stat" style="left:206px"><div class="stat-num">3314</div><div class="stat-label">Completed Projects</div></div>
  <div class="stat" style="left:362px"><div class="stat-num">3314</div><div class="stat-label">Happy Customers</div></div>
</section>
<div class="shadow-curve" style="top:1366px"></div>

<section class="who">
  <h2 class="section-title" style="top:1418px">Who We Are ?</h2>
  <p class="section-sub" style="top:1456px">Great Insights About Data &amp; Analytics</p>

  <div class="feed">
    <div class="feed-head">
      <span class="feed-title">Our Chirply Feeds</span>
      <span class="btn-follow">Follow Our Feeds</span>
    </div>
    <div class="feed-item" style="top:64px">
      <svg class="feed-icon" viewBox="0 0 42 42"><circle cx="21" cy="21" r="19" fill="#fff" stroke="var(--accent)" stroke-width="2"/><circle cx="21" cy="21" r="13" fill="var(--accent)"/></svg>
      <div class="feed-name">Ashgrove Hill College</div>
      <p class="feed-text">There are many variations of passages of Lorem Ipsum available, but the majority have suffered alteration in some form</p>
    </div>
    <div class="feed-item" style="top:145px">
      <svg class="feed-icon" viewBox="0 0 42 42"><circle cx="21" cy="21" r="19" fill="#fff" stroke="var(--accent)" stroke-width="2"/><circle cx="21" cy="21" r="13" fill="var(--accent)"/></svg>
      <div class="feed-name">Ashgrove Hill College</div>
      <p class="feed-text">There are many variations of passages of Lorem Ipsum available, but the majority have suffered alteration in some form</p>
    </div>
    <div class="feed-item" style="top:227px">
      <svg class="feed-icon" viewBox="0 0 42 42"><circle cx="21" cy="21" r="19" fill="#fff" stroke="var(--accent)" stroke-width="2"/><circle cx="21" cy="21" r="13" fill="var(--accent)"/></svg>
      <div class="feed-name">Ashgrove Hill College</div>
      <p class="feed-text">There are many variations of passages of Lorem Ipsum available, but the majority have suffered alteration in some form</p>
    </div>
  </div>

  <div class="quote-card"></div>
  <div class="quote-photo" role="img" aria-label="Black and white portrait of a smiling businesswoman"></div>
  <svg class="quote-open" style="left:881px;top:1534px" viewBox="0 0 24 20"><rect x="1" y="8" width="9" height="10" fill="#555"/><rect x="13" y="8" width="9" height="10" fill="#555"/><path d="M1 9 Q2 2 9 1 L9 4 Q5 5 5 9 Z M13 9 Q14 2 21 1 L21 4 Q17 5 17 9 Z" fill="#555"/></svg>
  <p class="quote-text">Contrary to the first of popular belief, Lorem the Ipsum is not simply random text. It has roots in a piece of classical Latin literature from 45 BC, making it over 2000 years old. Daniel It has roots in a piece</p>
  <svg class="quote-close" style="left:1047px;top:1720px" viewBox="0 0 24 20"><g transform="rotate(180 12 10)"><rect x="1" y="8" width="9" height="10" fill="#555"/><rect x="13" y="8" width="9" height="10" fill="#555"/><path d="M1 9 Q2 2 9 1 L9 4 Q5 5 5 9 Z M13 9 Q14 2 21 1 L21 4 Q17 5 17 9 Z" fill="#555"/></g></svg>
</section>

<section class="partners">
  <h2 class="partners-title">Our Partners Trust Us With Their Projects</h2>
  <div class="partner-badge" style="left:97px;width:96px"></div>
  <div class="partner-badge" style="left:250px;width:104px"></div>
  <div class="partner-badge" style="left:412px;width:90px"></div>
  <div class="partner-badge" style="left:563px;width:120px"></div>
  <div class="partner-badge" style="left:741px;width:130px"></div>
  <div class="partner-badge" style="left:936px;width:164px"></div>
</section>

<footer class="site-footer">
  <div class="footer-curve"></div>
  <h3 class="footer-heading" style="left:99px;top:36px">Contact Us On</h3>
  <div class="footer-label" style="left:99px;top:82px">Address :</div>
  <p class="footer-text" style="left:99px;top:112px;width:340px">7896 , Lorem Ipsum is simply dummy text of the printing a typese tting industry. dummy text</p>
  <div class="footer-label" style="left:99px;top:181px">Phone :</div>
  <p class="footer-text" style="left:99px;top:210px">+1 555 014 2230 / 555 019 8841</p>
  <div class="footer-label" style="left:291px;top:181px">Mail Id :</div>
  <p class="footer-text" style="left:291px;top:210px">info@marlowvane.co</p>
  <svg class="phone-badge" viewBox="0 0 72 72"><circle cx="36" cy="36" r="34" fill="#fff"/><circle cx="36" cy="36" r="26" fill="none" stroke="#222" stroke-width="2.5"/><path d="M27 24 Q25 26 26 30 Q30 42 42 47 Q46 48 48 45 L48 42 L42 39 L39 42 Q33 39 30 33 L33 30 L30 24 Z" fill="#222"/></svg>
  <h3 class="footer-heading" style="left:723px;top:36px">Subscribe To Newsletter</h3>
  <p class="footer-text" style="left:723px;top:80px;width:370px;color:#bbb">Lorem ipsum dolor sit amet, consectetur adipiscing elit, sed do eiusmod tempor incididunt ut labore et dolore magna</p>
  <div class="mail-input">Your Mail Id</div>
  <div class="btn-subscribe">Subscribe Now</div>
</footer>
<div class="footer-bar">Copyrights@2016 Company Name @ All Rights Reserved</div>

</body>
</html>
```